Cafe Menu for Maplebrook Lantern Cafe

Menu designed for my cafe. I need multiple sizes to be created.
DL pamphlet
A4
and I also need 5 x A3 portraits & 5 x A3 landscapes. The menu must be spread out over a total of 10 A3 pages. I have uploaded my logo which needs to be used & I would like the colours from the logo used. The background of the menu needs to be white. I have uploaded an image on another menu for which I would like the same heading font to be used.

Target Market(s)

cafe, restaurant

Font styles to use
Serif
Decorative
Script

Requirements
Must have
• White back ground
correct font as I have uploaded
Nice to have
• May have drawings of food in back and white.

```html
<!DOCTYPE html>
<html lang="en">
<head>
<meta charset="utf-8">
<title>Maplebrook Lantern Cafe – Menu</title>
<link href="https://fonts.googleapis.com/css2?family=Courgette&family=Roboto+Condensed:ital,wght@0,400;0,700;1,400&display=swap" rel="stylesheet">
<style>
:root{
  --stage:#e6e7e9;
  --paper:#ffffff;
  --charcoal:#3a3a3a;
  --olive:#8ea23a;
  --olive-dark:#7f9530;
  --sage-light:#b9c683;
  --ink:#1f1f1f;
  --ink-soft:#4a4a4a;
  --rule:#8a8a8a;
  --wash:#e6f1df;
  --foliage:#8fb49c;
  --sketch:#ecedea;
}
*{box-sizing:border-box;margin:0;padding:0}
html,body{width:1200px;height:1200px;overflow:hidden}
body{background:var(--stage);font-family:"Roboto Condensed",Arial,sans-serif;color:var(--ink);position:relative}
.sheet{position:absolute;top:244px;width:811px;height:1145px;background:var(--paper);transform:scale(.6214);transform-origin:0 0;box-shadow:6px 8px 14px rgba(0,0,0,.35);overflow:hidden}
.sheet--front{left:68px}
.sheet--back{left:628px}
.wash{position:absolute;background:var(--wash)}
.foliage{position:absolute;background:var(--foliage)}
.sketch{position:absolute;background:var(--sketch)}
.header-band{position:absolute;left:0;top:0;width:100%;background:var(--charcoal)}
.header-rule{position:absolute;left:0;width:100%;height:7px;background:var(--olive)}
.brand-seal{position:absolute;left:36px;top:30px;width:124px;height:124px;border-radius:50%;background:#fff;display:flex;flex-direction:column;align-items:center;justify-content:center;text-align:center;font-size:13px;color:var(--olive-dark);line-height:1.15;padding:10px}
.brand-seal .tag{color:var(--ink);font-size:10px;margin-top:6px}
.brand-seal .addr{color:var(--ink);font-size:7px;margin-top:6px}
.menu-title{position:absolute;left:195px;top:38px;font-family:"Courgette",cursive;font-size:72px;color:var(--sage-light);line-height:1}
.menu-phone{position:absolute;left:193px;top:113px;font-size:30px;color:var(--olive);letter-spacing:1px}
.hours{position:absolute;right:36px;top:78px;text-align:right;color:#fff;font-size:15px;line-height:20px}
.hours .email{color:var(--sage-light);font-weight:700}
.surcharge{position:absolute;right:36px;top:157px;color:#fff;font-style:italic;font-size:15px}
.section{position:absolute}
.section h2{font-family:"Courgette",cursive;font-weight:400;color:var(--olive);font-size:27px;line-height:1;margin-bottom:8px}
.section h3{font-size:14px;font-weight:700;color:var(--ink-soft);margin:-2px 0 4px}
.item{display:grid;grid-template-columns:1fr 58px;border-bottom:1px dashed var(--rule)}
.item:last-child{border-bottom:none}
.item-body{padding:3px 4px 3px 0}
.item-name{font-size:14px;line-height:16px}
.item-desc{font-size:10px;font-style:italic;color:var(--ink-soft);line-height:13px}
.item-price{border-left:1px dashed var(--rule);display:flex;align-items:center;justify-content:flex-end;font-size:14px}
.narrow .item{grid-template-columns:1fr 55px}
.narrow .item-body{padding:4px 4px 4px 0}
.site{position:absolute;left:0;width:811px;top:1098px;text-align:center;font-weight:700;font-size:14px;color:var(--ink)}
.info-box{position:absolute;left:87px;top:982px;width:305px;height:70px;background:var(--charcoal);color:#fff;font-size:15px;line-height:20px;padding:6px 14px}
.info-box .email{color:var(--sage-light);font-weight:700}
</style>
</head>
<body>

<!-- Front sheet: drinks -->
<section class="sheet sheet--front">
  <div class="wash" style="left:400px;top:192px;width:411px;height:880px" role="img" aria-label="pale green painted background"></div>
  <div class="wash" style="left:30px;top:860px;width:370px;height:210px" role="img" aria-label="pale green painted background"></div>

  <div class="header-band" style="height:185px"></div>
  <div class="header-rule" style="top:185px"></div>
  <div class="foliage" style="left:570px;top:0;width:241px;height:50px" role="img" aria-label="eucalyptus leaf garland"></div>

  <div class="brand-seal">
    <div>Maplebrook Lantern Cafe</div>
    <div class="tag">Coffee, breakfast &amp; lunch</div>
    <div class="addr">14 Harlow Street, Dunmore Q<br>Phone: 07 4510 2286</div>
  </div>
  <div class="menu-title">Menu</div>
  <div class="menu-phone">07 4510 2286</div>
  <div class="hours">Open 7 Days From 7am<br>Saturday &amp; Sunday 7am-12pm<br><span class="email">E: hello@maplebrooklantern.com.au</span></div>
  <div class="surcharge">10% Surcharge Applies on Sundays &amp; Public Holidays</div>

  <div class="sketch" style="left:32px;top:222px;width:50px;height:220px" role="img" aria-label="line drawings of milkshake and iced drinks"></div>
  <div class="sketch" style="left:32px;top:500px;width:50px;height:110px" role="img" aria-label="line drawing of a juice glass"></div>
  <div class="sketch" style="left:32px;top:630px;width:50px;height:210px" role="img" aria-label="line drawings of smoothies"></div>
  <div class="sketch" style="left:40px;top:910px;width:45px;height:150px" role="img" aria-label="line drawing of frappes"></div>
  <div class="sketch" style="left:715px;top:220px;width:60px;height:240px" role="img" aria-label="line drawings of coffee cup, beans and coffee sack"></div>
  <div class="sketch" style="left:715px;top:555px;width:60px;height:135px" role="img" aria-label="line drawing of takeaway cup and beans"></div>
  <div class="sketch" style="left:720px;top:710px;width:55px;height:80px" role="img" aria-label="line drawing of a milk jug"></div>
  <div class="sketch" style="left:700px;top:855px;width:80px;height:200px" role="img" aria-label="line drawings of a chicken and pancakes"></div>

  <div class="section" style="left:95px;top:222px;width:268px">
    <h2>Cold Drinks</h2>
    <div class="item"><div class="item-body"><div class="item-name">Milkshake</div></div><div class="item-price">$7.00</div></div>
    <div class="item"><div class="item-body"><div class="item-name">Thickshake</div><div class="item-desc">Flavours - Chocolate, vanilla, strawberry, banana, caramel &amp; coffee</div></div><div class="item-price">$8.00</div></div>
    <div class="item"><div class="item-body"><div class="item-name">Iced Latte</div><div class="item-desc">Add syrup: vanilla, caramel, white chocolate, hazelnut</div></div><div class="item-price">$7.50</div></div>
    <div class="item"><div class="item-body"><div class="item-name">Iced Coffee</div></div><div class="item-price">$8.00</div></div>
    <div class="item"><div class="item-body"><div class="item-name">Iced Chocolate</div></div><div class="item-price">$8.00</div></div>
    <div class="item"><div class="item-body"><div class="item-name">Iced Mocha</div></div><div class="item-price">$8.00</div></div>
  </div>

  <div class="section" style="left:95px;top:456px;width:268px">
    <h2 style="margin-bottom:18px">Juice Bar</h2>
    <div class="item"><div class="item-body"><div class="item-name">Passion Pop</div><div class="item-desc">Passionfruit, apple &amp; oranges</div></div><div class="item-price">$9.00</div></div>
    <div class="item"><div class="item-body"><div class="item-name">Sweet Juice</div><div class="item-desc">Apple, pineapple, oranges &amp; mango</div></div><div class="item-price">$9.00</div></div>
    <div class="item"><div class="item-body"><div class="item-name">Orange Juice</div><div class="item-desc">Freshly juiced oranges</div></div><div class="item-price">$9.00</div></div>
  </div>

  <div class="section" style="left:95px;top:632px;width:268px">
    <h2>Smoothies</h2>
    <div class="item"><div class="item-body"><div class="item-name">Mango Raspberry Smoothie</div><div class="item-desc">Frozen mango &amp; raspberry sorbet blended with coconut milk</div></div><div class="item-price">$9.00</div></div>
    <div class="item"><div class="item-body"><div class="item-name">Mango Coconut Smoothie</div><div class="item-desc">Frozen mango blended with coconut milk</div></div><div class="item-price">$9.00</div></div>
    <div class="item"><div class="item-body"><div class="item-name">Berry Blast Smoothie</div><div class="item-desc">Mixed berries blended with coconut milk</div></div><div class="item-price">$9.00</div></div>
    <div class="item"><div class="item-body"><div class="item-name">Choc Banana Smoothie</div><div class="item-desc">Frozen banana &amp; dark chocolate ice cream blended together with whole milk</div></div><div class="item-price">$9.00</div></div>
  </div>

  <div class="section" style="left:95px;top:868px;width:262px">
    <h2>Frappes</h2>
    <div class="item"><div class="item-body"><div class="item-name">Strawberry Lemonade Frappe</div><div class="item-desc">Strawberry syrup blended together with lemonade &amp; ice</div></div><div class="item-price">$9.00</div></div>
    <div class="item"><div class="item-body"><div class="item-name">Coffee Frappe</div><div class="item-desc">Espresso blended with milk &amp; ice, topped with cream</div></div><div class="item-price">$9.00</div></div>
    <div class="item"><div class="item-body"><div class="item-name">Chocolate Frappe</div><div class="item-desc">Chocolate syrup blended with milk &amp; ice, topped with cream</div></div><div class="item-price">$9.00</div></div>
  </div>

  <div class="section" style="left:447px;top:224px;width:268px">
    <h2>Coffee Menu</h2>
    <h3>Coffee &amp; Hot Drinks</h3>
    <div class="item"><div class="item-body"><div class="item-name">Cappuccino</div></div><div class="item-price">$4.80</div></div>
    <div class="item"><div class="item-body"><div class="item-name">Flat White</div></div><div class="item-price">$4.80</div></div>
    <div class="item"><div class="item-body"><div class="item-name">Latte</div></div><div class="item-price">$5.00</div></div>
    <div class="item"><div class="item-body"><div class="item-name">Long Black</div></div><div class="item-price">$4.80</div></div>
    <div class="item"><div class="item-body"><div class="item-name">Mocha</div></div><div class="item-price">$5.20</div></div>
    <div class="item"><div class="item-body"><div class="item-name">Macchiato</div></div><div class="item-price">$3.50</div></div>
    <div class="item"><div class="item-body"><div class="item-name">Espresso</div></div><div class="item-price">$3.50</div></div>
    <div class="item"><div class="item-body"><div class="item-name">Chai Latte</div></div><div class="item-price">$4.80</div></div>
    <div class="item"><div class="item-body"><div class="item-name">Hot Chocolate</div></div><div class="item-price">$4.80</div></div>
    <div class="item"><div class="item-body"><div class="item-name">Tea</div><div class="item-desc">Tea Flavours: English breakfast, earl grey, green, berry green &amp; coconut</div></div><div class="item-price">$4.50</div></div>
  </div>

  <div class="section" style="left:447px;top:555px;width:268px">
    <h2>Takeaway Coffee</h2>
    <div class="item"><div class="item-body"><div class="item-name">Takeaway Large</div></div><div class="item-price">$6.80</div></div>
    <div class="item"><div class="item-body"><div class="item-name">Takeaway Regular</div></div><div class="item-price">$5.20</div></div>
    <div class="item"><div class="item-body"><div class="item-name">Takeaway Small</div></div><div class="item-price">$4.80</div></div>
  </div>

  <div class="section" style="left:447px;top:689px;width:268px">
    <h2>Coffee Extras</h2>
    <div class="item"><div class="item-body"><div class="item-name">Mug &amp; Extra Shot</div></div><div class="item-price">50c</div></div>
    <div class="item"><div class="item-body"><div class="item-name">Soy &amp; Lactose Free Milk</div></div><div class="item-price">80c</div></div>
    <div class="item"><div class="item-body"><div class="item-name">Syrups</div><div class="item-desc">Flavours - Vanilla, caramel, hazelnut &amp; white chocolate</div></div><div class="item-price">$1.00</div></div>
  </div>

  <div class="section" style="left:447px;top:867px;width:268px">
    <h2>Kids Menu</h2>
    <div class="item"><div class="item-body"><div class="item-name">Scrambled Eggs</div><div class="item-desc">Two eggs scrambled with toast &amp; tomato sauce</div></div><div class="item-price">$9.50</div></div>
    <div class="item"><div class="item-body"><div class="item-name">Rainbow Pancakes</div><div class="item-desc">Two small pancakes served with ice cream &amp; sprinkles</div></div><div class="item-price">$9.50</div></div>
    <div class="item"><div class="item-body"><div class="item-name">Nuggets &amp; Chips</div></div><div class="item-price">$8.00</div></div>
    <div class="item"><div class="item-body"><div class="item-name">Chicken Chippees</div></div><div class="item-price">$8.50</div></div>
  </div>

  <div class="foliage" style="left:0;top:1080px;width:220px;height:65px" role="img" aria-label="eucalyptus leaf garland"></div>
  <div class="foliage" style="left:580px;top:1075px;width:231px;height:70px" role="img" aria-label="eucalyptus leaf garland"></div>
  <div class="site">www.maplebrooklanterncafe.com.au</div>
</section>

<!-- Back sheet: food -->
<section class="sheet sheet--back">
  <div class="wash" style="left:0;top:45px;width:811px;height:1030px" role="img" aria-label="pale green painted background"></div>

  <div class="header-band" style="height:38px"></div>
  <div class="header-rule" style="top:38px"></div>
  <div class="foliage" style="left:45px;top:0;width:190px;height:50px" role="img" aria-label="eucalyptus leaf garland"></div>
  <div class="foliage" style="left:540px;top:0;width:271px;height:50px" role="img" aria-label="eucalyptus leaf garland"></div>

  <div class="sketch" style="left:8px;top:130px;width:72px;height:630px" role="img" aria-label="line drawings of bacon, sausages, eggs, avocado and pancakes"></div>
  <div class="sketch" style="left:8px;top:780px;width:72px;height:210px" role="img" aria-label="line drawings of salad greens and herbs"></div>
  <div class="sketch" style="left:732px;top:115px;width:75px;height:530px" role="img" aria-label="line drawings of chicken, potatoes, avocado, sandwich and vegetables"></div>
  <div class="sketch" style="left:732px;top:690px;width:75px;height:360px" role="img" aria-label="line drawings of burgers, tomato and cow"></div>

  <div class="section narrow" style="left:88px;top:93px;width:307px">
    <h2>Breakfast Menu</h2>
    <div class="item"><div class="item-body"><div class="item-name">Big Breakfast</div><div class="item-desc">Bacon, sausages, hash browns, tomato, baked beans &amp; mushrooms with a slice of toasted panini bread &amp; your choice of fried, poached or scrambled eggs.</div></div><div class="item-price">$21.50</div></div>
    <div class="item"><div class="item-body"><div class="item-name">Classic Breakfast</div><div class="item-desc">Your choice of fried poached or scrambled eggs served with either bacon or sausages, tomato &amp; a slice of panini toast</div></div><div class="item-price">$16.50</div></div>
    <div class="item"><div class="item-body"><div class="item-name">Avocado Stack</div><div class="item-desc">Turkish bread topped with avocado, bacon or salmon, 2 poached eggs &amp; a sprinkle of feta cheese</div></div><div class="item-price">$17.00</div></div>
    <div class="item"><div class="item-body"><div class="item-name">Eggs Benedict</div><div class="item-desc">Your choice of bacon, ham or salmon served with toasted turkish bread, poached eggs &amp; creamy hollandaise sauce</div></div><div class="item-price">$19.00</div></div>
    <div class="item"><div class="item-body"><div class="item-name">Classic Omelet</div><div class="item-desc">Ham, tomato, spinach, onion &amp; cheese omelet topped with fried cherry tomatoes &amp; turkish toast</div></div><div class="item-price">$17.50</div></div>
    <div class="item"><div class="item-body"><div class="item-name">Panini Scramble</div><div class="item-desc">Toasted panini bread topped with scrambled eggs, sautéed mushrooms, cherry tomatoes &amp; spinach with a drizzle of hollandaise sauce on top</div></div><div class="item-price">$16.50</div></div>
    <div class="item"><div class="item-body"><div class="item-name">Breaky Wrap</div><div class="item-desc">Bacon, eggs, hash browns, cheese &amp; BBQ sauce on a toasted wrap</div></div><div class="item-price">$15.00</div></div>
    <div class="item"><div class="item-body"><div class="item-name">Ultimate Breakfast Toastie</div><div class="item-desc">Bacon, scrambled eggs, smashed avocado, spinach &amp; feta with hollandaise sauce on a toasted ciabatta sandwich roll</div></div><div class="item-price">$14.50</div></div>
    <div class="item"><div class="item-body"><div class="item-name">Breakfast Share Plate</div><div class="item-desc">A delicious selection of yummy breakfast items including bacon, scrambled eggs, hash browns, croissant, yogurt, strawberries &amp; blueberries.</div></div><div class="item-price">$28.50</div></div>
    <div class="item"><div class="item-body"><div class="item-name">Fruity Pancakes</div><div class="item-desc">3 fluffy pancakes topped with a tropical fruit mix including strawberries, mango &amp; blueberries with a sprinkle of icing sugar, served with maple syrup.</div></div><div class="item-price">$17.50</div></div>
    <div class="item"><div class="item-body"><div class="item-name">Bacon Avocado Salsa</div><div class="item-desc">Smashed avocado topped with diced tomato &amp; bacon with spinach, a sprinkle of feta, a side of hash browns &amp; a wedge of lemon</div></div><div class="item-price">$17.50</div></div>
  </div>

  <div class="section narrow" style="left:88px;top:780px;width:307px">
    <h2>Salads</h2>
    <div class="item"><div class="item-body"><div class="item-name">Caesar Salad</div><div class="item-desc">Chicken breast with lettuce, bacon, egg, parmesan cheese, croutons &amp; caesar dressing</div></div><div class="item-price">$16.50</div></div>
    <div class="item"><div class="item-body"><div class="item-name">Mango Chicken Salad</div><div class="item-desc">Chicken breast, lettuce, mango, onion &amp; cashews with a creamy curry dressing</div></div><div class="item-price">$16.50</div></div>
    <div class="item"><div class="item-body"><div class="item-name">Tropical Prawn Salad</div><div class="item-desc">Cooked prawns with avocado, tomato, cucumber and mango salsa mixed through with mixed lettuce and poppyseed dressing.</div></div><div class="item-price">$17.50</div></div>
  </div>

  <div class="info-box">Open 7 Days From 7am<br>Saturday &amp; Sunday 7am-12pm<br><span class="email">E: hello@maplebrooklantern.com.au</span></div>

  <div class="section narrow" style="left:422px;top:93px;width:306px">
    <h2>Lunch Menu</h2>
    <div class="item"><div class="item-body"><div class="item-name">Parmi Turkish Roll</div><div class="item-desc">Chicken tenders, tomato relish, cheese, lettuce &amp; herb mayo served on a toasted turkish roll with a side of chips</div></div><div class="item-price">$16.50</div></div>
    <div class="item"><div class="item-body"><div class="item-name">Sweet Potato Chips</div><div class="item-desc">Seasoned sweet potato chips served with a herb mayonnaise</div></div><div class="item-price">$13.50</div></div>
    <div class="item"><div class="item-body"><div class="item-name">Chicken Avocado Panini Grill</div><div class="item-desc">Chicken, avocado, cheese &amp; aioli served on toasted panini bread &amp; grilled with a side of chips</div></div><div class="item-price">$15.50</div></div>
    <div class="item"><div class="item-body"><div class="item-name">Steak Sandwich</div><div class="item-desc">Fillet steak with salad, cheese &amp; BBQ sauce on toasted bread with a side of chips</div></div><div class="item-price">$17.50</div></div>
    <div class="item"><div class="item-body"><div class="item-name">Club Sandwich</div><div class="item-desc">Three slices of toasted bread with ham, bacon, chicken, tomato, cheese, lettuce &amp; mayonnaise with a side of chips</div></div><div class="item-price">$16.50</div></div>
    <div class="item"><div class="item-body"><div class="item-name">Fresh or Toasted Sandwich</div><div class="item-desc">Your choice of meat, salad &amp; sauce on fresh white or wholemeal bread toasted or fresh</div></div><div class="item-price">$8.00</div></div>
    <div class="item"><div class="item-body"><div class="item-name">Pulled Pork Turkish Roll</div><div class="item-desc">Pulled pork mixed with gravy, house made coleslaw, lettuce &amp; herb mayonnaise on a toasted turkish roll with a side of chips</div></div><div class="item-price">$15.50</div></div>
    <div class="item"><div class="item-body"><div class="item-name">Fish, Chips &amp; Salad</div><div class="item-desc">Battered fillets with chips &amp; salad, herb mayonnaise, lemon &amp; salad dressing.</div></div><div class="item-price">$17.50</div></div>
    <div class="item"><div class="item-body"><div class="item-name">Nachos</div><div class="item-desc">Nacho chips topped with nacho mince, cheese sauce, melted cheese, diced tomato &amp; smashed avocado.</div></div><div class="item-price">$16.50</div></div>
    <div class="item"><div class="item-body"><div class="item-name">Lunch Bruschetta</div><div class="item-desc">Toasted sourdough bread with avocado, cherry tomatoes, onion, feta &amp; a drizzle of balsamic glaze with a side of chips</div></div><div class="item-price">$16.50</div></div>
  </div>

  <div class="section narrow" style="left:424px;top:666px;width:304px">
    <h2>Burgers</h2>
    <div class="item"><div class="item-body"><div class="item-name">The Roadhouse Burger</div><div class="item-desc">Mince patty, burger cheese, fries, bbq sauce &amp; pickles with a side of chips</div></div><div class="item-price">$17.50</div></div>
    <div class="item"><div class="item-body"><div class="item-name">The Gringo Burger</div><div class="item-desc">Ask sam what to put in this one</div></div><div class="item-price">$18.50</div></div>
    <div class="item"><div class="item-body"><div class="item-name">Barramundi Burger</div><div class="item-desc">Crispy barramundi fillet with lettuce, tomato, onion, cheese &amp; tartare sauce served with chips</div></div><div class="item-price">$16.50</div></div>
    <div class="item"><div class="item-body"><div class="item-name">Beef Burger</div><div class="item-desc">Steak or mince with salad, cheese &amp; BBQ sauce with a side of chips<br>Add Bacon $2.00 ~ Add Egg $2.00</div></div><div class="item-price">$15.50</div></div>
    <div class="item"><div class="item-body"><div class="item-name">Ultimate Chicken Burger</div><div class="item-desc">Southern style chicken patty with bacon, pineapple, salad, cheese &amp; mayonnaise with a side of chips</div></div><div class="item-price">$17.00</div></div>
    <div class="item"><div class="item-body"><div class="item-name">Chicken Avocado Burger</div><div class="item-desc">Southern style chicken patty with bacon, avocado, lettuce, tomato, cheese &amp; mayonnaise with a side of chips</div></div><div class="item-price">$17.00</div></div>
    <div class="item"><div class="item-body"><div class="item-name">Herb Chicken Burger</div><div class="item-desc">Southern style chicken patty with bacon, avocado, cheese, lettuce, tomato, onion, tomato relish &amp; a delicious homemade herb mayonnaise with a side of chips</div></div><div class="item-price">$17.00</div></div>
  </div>

  <div class="foliage" style="left:0;top:1080px;width:215px;height:65px" role="img" aria-label="eucalyptus leaf garland"></div>
  <div class="foliage" style="left:570px;top:1075px;width:241px;height:70px" role="img" aria-label="eucalyptus leaf garland"></div>
  <div class="site">www.maplebrooklanterncafe.com.au</div>
</section>

</body>
</html>
```